Holloway-Prentiss & Associates
Business card & Word template design
Draft #12:
I like the shading -- it gives it dimension. But I would prefer a solid blue bar along the bottom (rather than a blue /black bar). I also like the back side of the bottom card. Could you remove the words "Financial Planning & Wealth Advisors" from the logo to make it look less busy?
Draft #10: Please see comments for Draft #11, as they apply as well. I like the wave on this one! One thought - could you put the phone and fax number on the same line to reduce the number of horizontal lines and create more balance for the long email address line?
Draft #11:
Nice work! I like the placement of the logo on the all-cap version (the design that has the logo on the left and more centered vertically). I like the shape of the all-cap letters but they seem lighter and not as easy to read(don't pop out as much as the other font). Could I please see a version that has the non-cap (darker) font on the layout with the logo on the left? Also, could you remove the word "email" from before the email address?
Draft #18 - additional note -- could you also please remove the comma after "Suite 485" in the address if it's on two different lines?
Draft #18:
Nice work! I like the blue area. I don't need the URL on the card, but I do need the words "Registered Investment Advisor" and "Financial Planning & Fee-Only Investments". Also, I like the line spacing on the address better than the line spacing on the phone/fax/email side of the card.
Nice work!
I am a little concerned with font being too small or narrow to be easily readable. I would like to see another font that has wider letters or perhaps the all-caps like the logo?
Also, I like to spell out "phone" and "fax" but not need an "e" or "email" for the email address.
Also, I would need the words "Registered Investment Advisor" and "Financial Planning & Fee-Only Investments" on the front (I'm looking for a single-sided card). If there's not enough space, can the words "Financial Planning and Wealth Advisors" be removed from the logo graphic to make more room?

```html
<!DOCTYPE html>
<html lang="en">
<head>
<meta charset="utf-8">
<title>Holloway-Prentiss &amp; Associates — Business Card</title>
<link rel="stylesheet" href="https://fonts.googleapis.com/css2?family=Cormorant+SC:wght@500;600;700&display=swap">
<style>
  :root {
    --backdrop: #e4e6e9;
    --card-top: #ffffff;
    --card-bottom: #eef0f2;
    --brand-blue: #1f6fb5;
    --brand-navy: #1d3f6e;
    --ink: #2e3338;
    --shade-dark: #3b3f44;
    --shade-light: #9aa0a6;
    --band-text: #ffffff;
  }
  html, body {
    margin: 0;
    width: 1200px;
    height: 794px;
    overflow: hidden;
    background: var(--backdrop);
    font-family: "Cormorant SC", "Times New Roman", serif;
  }
  .canvas {
    position: relative;
    width: 1200px;
    height: 794px;
  }
  .business-card {
    position: absolute;
    left: 150px;
    top: 140px;
    width: 900px;
    height: 514px;
    border-radius: 10px;
    overflow: hidden;
    background: linear-gradient(160deg, var(--card-top) 0%, var(--card-top) 45%, var(--card-bottom) 100%);
    box-shadow: 0 18px 40px rgba(0,0,0,0.18);
  }
  .brand {
    position: absolute;
    left: 56px;
    top: 92px;
    display: flex;
    align-items: center;
    gap: 18px;
  }
  .brand-square {
    width: 34px;
    height: 34px;
    background: var(--brand-navy);
  }
  .brand-name {
    color: var(--brand-navy);
    font-weight: 600;
    font-size: 36px;
    line-height: 1.05;
    letter-spacing: 0.5px;
  }
  .holder {
    position: absolute;
    right: 62px;
    top: 58px;
    text-align: right;
  }
  .holder-name {
    color: var(--brand-blue);
    font-weight: 700;
    font-size: 27px;
    letter-spacing: 0.5px;
  }
  .holder-title {
    color: var(--ink);
    font-weight: 600;
    font-size: 20px;
    margin-top: 2px;
    letter-spacing: 1px;
  }
  .contact {
    position: absolute;
    right: 62px;
    top: 200px;
    text-align: right;
    color: var(--ink);
    font-weight: 600;
    font-size: 19px;
    letter-spacing: 0.6px;
  }
  .address { line-height: 1.45; }
  .reach { margin-top: 20px; line-height: 1.3; }
  .wave {
    position: absolute;
    left: 0;
    bottom: 0;
    width: 900px;
    height: 514px;
  }
  .credentials {
    position: absolute;
    right: 62px;
    bottom: 22px;
    text-align: right;
    color: var(--band-text);
    font-weight: 700;
    font-size: 20px;
    line-height: 1.3;
    letter-spacing: 0.8px;
  }
</style>
</head>
<body>
<main class="canvas">
  <article class="business-card">
    <svg class="wave" viewBox="0 0 900 514" aria-hidden="true">
      <defs>
        <linearGradient id="shade" x1="0" y1="0" x2="1" y2="0">
          <stop offset="0" stop-color="var(--shade-dark)"/>
          <stop offset="1" stop-color="var(--shade-light)"/>
        </linearGradient>
      </defs>
      <path d="M0,440 C260,386 560,372 900,368 L900,400 C560,404 260,420 0,470 Z" fill="url(#shade)"/>
      <path d="M0,470 C260,420 560,404 900,400 L900,514 L0,514 Z" fill="var(--brand-blue)"/>
    </svg>

    <div class="brand">
      <span class="brand-square"></span>
      <span class="brand-name">Holloway-Prentiss<br>&amp; Associates</span>
    </div>

    <header class="holder">
      <div class="holder-name">Marian Holloway-Prentiss</div>
      <div class="holder-title">Principal</div>
    </header>

    <section class="contact">
      <div class="address">72 Alder Street, Suite 485<br>Ridgemont, CA 94110</div>
      <div class="reach">Phone: 555.014.2288 &nbsp;|&nbsp; Fax: 555.014.2290<br>marian@holloway-prentiss-associates.com</div>
    </section>

    <footer class="credentials">
      Registered Investment Advisor<br>
      Financial Planning &amp; Fee-Only Investments
    </footer>
  </article>
</main>
</body>
</html>
```